Amber Ridge Publishing Web Page Design

Design a website for my new start up publishing company - Amber Ridge Publishing, the first work published by ARP with be a new book by M.R. Theodor called Silent Ledger. The prototype for the book cover is attached.

Target Market(s)

Worldwide, all readers of mystery, fiction, etc.

Industry/Entity Type

Book Publisher

Coding

Coded - Design and coding required

Number of Pages Required

1 page

```html
<!DOCTYPE html>
<html lang="en">
<head>
<meta charset="utf-8">
<title>Amber Ridge Publishing</title>
<link href="https://fonts.googleapis.com/css2?family=Archivo+Black&family=Open+Sans:wght@400;600;700&display=swap" rel="stylesheet">
<style>
  :root {
    --ink: #0b0b0d;
    --teal: #1ea6b8;
    --white: #ffffff;
    --muted: #b9b9be;
    --red: #c8261c;
    --blood: #5a0c0c;
    --gold: #f2c318;
    --fb: #3b5998;
  }
  * { box-sizing: border-box; margin: 0; padding: 0; }
  html, body { width: 1200px; height: 2332px; overflow: hidden; }
  body {
    position: relative;
    background: var(--ink);
    font-family: "Open Sans", Arial, sans-serif;
    color: var(--white);
  }
  .abs { position: absolute; }

  .hero-scene {
    left: 0; top: 0; width: 1200px; height: 640px;
    background:
      radial-gradient(ellipse 260px 200px at 560px 270px, rgba(120,20,20,.55), transparent 70%),
      radial-gradient(ellipse 420px 260px at 880px 330px, rgba(60,70,90,.55), transparent 70%),
      radial-gradient(ellipse 300px 300px at 150px 420px, rgba(110,10,10,.6), transparent 70%),
      linear-gradient(180deg, #121216 0%, #1c1416 55%, var(--ink) 100%);
  }
  .story-bg {
    left: 0; top: 640px; width: 1200px; height: 460px;
    background:
      radial-gradient(ellipse 380px 200px at 900px 120px, rgba(110,15,15,.35), transparent 70%),
      linear-gradient(180deg, var(--ink) 0%, #111114 100%);
  }

  .brand { text-align: center; }
  .brand-dot {
    display: block; margin: 0 auto 8px;
    border: 3px solid var(--white); border-radius: 50%;
  }
  .brand-name {
    font-family: "Archivo Black", sans-serif; color: var(--white);
    letter-spacing: 1px; line-height: 1.3;
  }
  .header-brand { left: 30px; top: 14px; width: 170px; }
  .header-brand .brand-dot { width: 46px; height: 46px; }
  .header-brand .brand-name { font-size: 11px; }

  .social-note {
    left: 40px; top: 118px; display: flex; align-items: center; gap: 8px; font-size: 11px;
  }
  .social-note .dot { width: 14px; height: 14px; background: var(--fb); border-radius: 2px; }

  .nav {
    right: 60px; top: 48px; display: flex; gap: 26px;
    font-weight: 700; font-size: 14px; letter-spacing: .5px;
  }

  .tagline {
    left: 640px; top: 148px; width: 540px; text-align: center;
    font-family: "Archivo Black", sans-serif; color: var(--teal);
    font-size: 38px; line-height: 1.15; text-transform: uppercase; white-space: nowrap;
  }

  .book { box-shadow: 8px 10px 24px rgba(0,0,0,.7); overflow: hidden; }
  .book-cover {
    width: 100%; height: 100%; position: relative;
    background:
      radial-gradient(ellipse 60% 35% at 50% 70%, rgba(140,150,230,.6), transparent 70%),
      linear-gradient(180deg, #16234a 0%, #2b3f86 55%, #141b3a 100%);
  }
  .book-title {
    position: absolute; left: 0; right: 0; top: 14%;
    text-align: center; font-family: "Archivo Black", sans-serif;
    color: #d7ecff; line-height: 1; text-transform: uppercase;
  }
  .book-author {
    position: absolute; left: 0; right: 0; bottom: 5%;
    text-align: center; font-weight: 700; font-size: 12px; color: #e8e8f0;
  }

  .btn-outline {
    border: 1px solid var(--muted); background: rgba(0,0,0,.6);
    font-size: 12px; font-weight: 600; letter-spacing: .5px;
    text-align: center; line-height: 36px; height: 38px;
  }

  .section-title {
    font-family: "Archivo Black", sans-serif; color: var(--teal);
    font-size: 42px; text-transform: uppercase; letter-spacing: .5px;
  }
  .sub-title { font-family: "Archivo Black", sans-serif; font-size: 34px; text-transform: uppercase; }
  .body-copy { font-size: 15px; line-height: 1.55; color: var(--muted); width: 430px; }

  .store-cover { box-shadow: 6px 8px 20px rgba(0,0,0,.7); }
  .btn-red {
    background: var(--red); font-size: 12px; font-weight: 700; letter-spacing: .5px;
    text-align: center; line-height: 36px; height: 36px; width: 150px;
  }

  .feedback-band {
    left: 0; top: 1728px; width: 1200px; height: 296px;
    background:
      radial-gradient(ellipse 300px 160px at 200px 140px, rgba(150,20,20,.55), transparent 70%),
      radial-gradient(ellipse 300px 160px at 1000px 160px, rgba(150,20,20,.5), transparent 70%),
      linear-gradient(180deg, #2a0a0a 0%, var(--blood) 50%, #240808 100%);
  }
  .feedback-title {
    left: 0; top: 1740px; width: 1200px; text-align: center;
    font-family: "Archivo Black", sans-serif; font-size: 44px; line-height: 1.08; text-transform: uppercase;
  }
  .feedback-email {
    left: 0; top: 1838px; width: 1200px; text-align: center;
    font-weight: 700; font-size: 40px; color: var(--gold);
  }

  .footer-brand { left: 500px; top: 2046px; width: 200px; }
  .footer-brand .brand-dot { width: 80px; height: 80px; border-width: 4px; }
  .footer-brand .brand-name { font-size: 13px; }

  .copyright { left: 140px; top: 2212px; font-size: 11px; color: var(--muted); }
  .stores { left: 516px; top: 2196px; display: flex; gap: 14px; }
  .stores span { width: 46px; height: 46px; border-radius: 50%; background: #e9e9ee; display: block; }
  .socials { left: 912px; top: 2212px; display: flex; gap: 18px; }
  .socials span { width: 12px; height: 12px; background: var(--white); display: block; }
</style>
</head>
<body>
  <div class="abs hero-scene" role="img" aria-label="Night scene with a dark castle, full moon and red mist"></div>
  <div class="abs story-bg"></div>

  <div class="abs brand header-brand">
    <span class="brand-dot"></span>
    <div class="brand-name">AMBER RIDGE<br>PUBLISHING</div>
  </div>
  <div class="abs social-note"><span class="dot"></span>Coming Soon</div>

  <nav class="abs nav">
    <span>HOME</span><span>NEW RELEASE</span><span>FREE SAMPLE</span><span>COMING SOON</span>
  </nav>

  <h1 class="abs tagline">Mystery &amp;<br>Suspense live here</h1>

  <div class="abs book" style="left:100px;top:176px;width:260px;height:370px;">
    <div class="book-cover" role="img" aria-label="Cover art: stormy blue night with lightning over a city">
      <div class="book-title" style="font-size:40px;">Silent<br>Ledger</div>
      <div class="book-author">M.R. THEODOR</div>
    </div>
  </div>
  <div class="abs btn-outline" style="left:122px;top:566px;width:156px;">FREE SAMPLE</div>

  <h2 class="abs section-title" style="left:140px;top:718px;">The Story</h2>
  <h3 class="abs sub-title" style="left:140px;top:778px;">Overview /Synopsis</h3>
  <p class="abs body-copy" style="left:140px;top:846px;">I am text block. Click edit button to change this text. Lorem ipsum dolor sit amet, consectetur adipiscing elit. Ut elit tellus, luctus nec ullamcorper mattis, pulvinar dapibus leo. I am text block. Click edit button to change this text. Lorem ipsum dolor sit amet, consectetur adipiscing elit. Ut elit tellus, luctus nec ullamcorper mattis, pulvinar dapibus leo.</p>

  <div class="abs book" style="left:742px;top:640px;width:230px;height:330px;">
    <div class="book-cover" role="img" aria-label="Cover art: stormy blue night with lightning over a city">
      <div class="book-title" style="font-size:36px;">Silent<br>Ledger</div>
      <div class="book-author">M.R. THEODOR</div>
    </div>
  </div>
  <div class="abs btn-outline" style="left:780px;top:1012px;width:160px;">FREE SAMPLE</div>

  <h2 class="abs section-title" style="left:160px;top:1128px;">Where to buy</h2>

  <div class="abs store-cover" role="img" aria-label="Book cover: haunted house under a purple sky" style="left:146px;top:1200px;width:190px;height:290px;background:linear-gradient(180deg,#3a2a48 0%,#6a4a5a 45%,#1a1418 100%);"></div>
  <div class="abs store-cover" role="img" aria-label="Book cover: dark tree and manor at night" style="left:482px;top:1200px;width:190px;height:290px;background:linear-gradient(180deg,#0f1c2c 0%,#2a4260 50%,#0a0f16 100%);"></div>
  <div class="abs store-cover" role="img" aria-label="Book cover: figure walking toward glowing city lights" style="left:818px;top:1200px;width:190px;height:290px;background:linear-gradient(180deg,#1c2448 0%,#4a5a9a 45%,#c07a4a 80%,#1a1420 100%);"></div>

  <div class="abs btn-red" style="left:166px;top:1548px;">HARD COPY</div>
  <div class="abs btn-red" style="left:502px;top:1548px;">PAPERBACK</div>
  <div class="abs btn-red" style="left:838px;top:1548px;">EBOOK</div>

  <div class="abs feedback-band" role="img" aria-label="Blood red grunge texture"></div>
  <h2 class="abs feedback-title">Provide Feedback<br>Send a review</h2>
  <div class="abs feedback-email">admin@amberridgepub.com</div>

  <div class="abs brand footer-brand">
    <span class="brand-dot"></span>
    <div class="brand-name">AMBER RIDGE<br>PUBLISHING</div>
  </div>

  <div class="abs copyright">Copyright © 2019 ARP. All Rights Reserved.</div>
  <div class="abs stores" aria-label="Online stores"><span></span><span></span><span></span></div>
  <div class="abs socials" aria-label="Social links"><span></span><span></span></div>
</body>
</html>
```